Business Card Design Project

www.plenvaportal.com is our website. We are a technology company that provides brokers, lawyers and accountants with an cloud based paperless facilitation and revenue stream that facilitates their clients Health spending accounts.

Target Market(s)

Insurance brokers, lawyers and accountants

Industry/Entity Type

Business

```html
<!DOCTYPE html>
<html lang="en">
<head>
<meta charset="utf-8">
<title>Plenva Business Card</title>
<link rel="stylesheet" href="https://fonts.googleapis.com/css2?family=Open+Sans:wght@700&family=PT+Sans+Narrow:wght@400;700&display=swap">
<style>
  :root {
    --navy: #02558f;
    --sky: #29abe2;
    --white: #ffffff;
    --edge: #1a1a1a;
    --page: #ffffff;
  }
  html, body {
    margin: 0;
    padding: 0;
    width: 1200px;
    height: 912px;
    overflow: hidden;
    background: var(--page);
  }
  .canvas {
    position: relative;
    width: 1200px;
    height: 912px;
  }
  .card {
    position: absolute;
    width: 601px;
    height: 388px;
    box-sizing: border-box;
    border: 1px solid var(--edge);
    overflow: hidden;
  }
  .card--front { left: 177px; top: 35px; background: var(--white); }
  .card--back  { left: 428px; top: 460px; background: var(--navy); }

  .brand-panel {
    position: absolute;
    left: 0; top: 0;
    width: 317px; height: 100%;
    display: flex;
    flex-direction: column;
    align-items: center;
    justify-content: center;
  }
  .contact-panel {
    position: absolute;
    left: 317px; top: 0;
    right: 0; height: 100%;
    background: var(--navy);
  }
  .wordmark {
    display: flex;
    align-items: center;
    gap: 14px;
    font-family: "PT Sans Narrow", sans-serif;
    font-weight: 700;
    font-size: 76px;
    line-height: 1;
    color: var(--sky);
  }
  .wordmark__dot {
    width: 40px; height: 40px;
    border-radius: 50%;
    background: var(--sky);
  }
  .website {
    margin-top: 26px;
    font-family: "PT Sans Narrow", sans-serif;
    font-size: 23px;
    color: var(--sky);
  }
  .card--back .brand-panel { width: 100%; padding-top: 40px; box-sizing: border-box; }
  .card--back .website { color: var(--white); }

  .contact {
    position: absolute;
    right: 37px;
    top: 134px;
    text-align: right;
    color: var(--white);
    font-family: "PT Sans Narrow", sans-serif;
    font-size: 21px;
    line-height: 27px;
  }
  .contact__name {
    margin: 0 0 2px;
    font-family: "Open Sans", sans-serif;
    font-weight: 700;
    font-size: 32px;
    line-height: 38px;
  }
  .contact__line { margin: 0; }
  .accent-bar {
    position: absolute;
    right: 0;
    top: 127px;
    width: 21px;
    height: 143px;
    background: var(--sky);
  }
</style>
</head>
<body>
<main class="canvas">
  <section class="card card--front">
    <div class="brand-panel">
      <div class="wordmark"><span class="wordmark__dot"></span>Plenva</div>
      <div class="website">www.plenvaportal.com</div>
    </div>
    <div class="contact-panel">
      <div class="contact">
        <p class="contact__name">Mara Lindqvist</p>
        <p class="contact__line">Suite 210, 4427 - 5th Avenue NW</p>
        <p class="contact__line">Calgary, AB T3B 2K4</p>
        <p class="contact__line">sales@plenvaportal.com</p>
        <p class="contact__line">admin@plenvaportal.com</p>
      </div>
      <div class="accent-bar"></div>
    </div>
  </section>

  <section class="card card--back">
    <div class="brand-panel">
      <div class="wordmark"><span class="wordmark__dot"></span>Plenva</div>
      <div class="website">www.plenvaportal.com</div>
    </div>
  </section>
</main>
</body>
</html>
```